Travel Agency Website - Simple General

Need a 7 page simple design that is pretty repetitive. Need to be able to load quickly that is SEO optimized. Trying to give ideas on what they can do, be personal as we are local, but at the same time come across as professional and get information easily with little burden.

- Landing Page
- Brambleton Vacations Page
- Family Trips
- Road Trips from Texas
- Other Destinations
- About Us Page
- Contact Us Page

Target Market(s)

Families

Coding

Coded - Design and coding required

Number of Pages Required

5+ page

Colors

Designer to choose colors to be used in the design.

Requirements
Must have
• Like it to flow easily with our logo. Use that for colors, etc.

```html
<!DOCTYPE html>
<html lang="en">
<head>
<meta charset="utf-8">
<title>Wayfarer Travel Co. — Helping Texas Families Create Magical Vacations</title>
<link rel="stylesheet" href="https://fonts.googleapis.com/css2?family=Roboto:wght@300;400;500;700;900&family=Heebo:wght@300;400;700&family=Libre+Baskerville:ital,wght@0,400;0,700;1,400&display=swap">
<style>
:root{
  --gold:#b47510;
  --teal:#1d6a6c;
  --ink:#1f1f1f;
  --text:#6b6b6b;
  --muted:#9a9a9a;
  --footer:#f3f3f3;
  --white:#ffffff;
}
*{box-sizing:border-box;margin:0;padding:0}
html,body{width:1200px;height:3612px;overflow:hidden}
body{position:relative;background:var(--white);font-family:"Roboto",sans-serif;color:var(--ink)}
.abs{position:absolute}
a{color:inherit;text-decoration:none}

/* Hero */
.hero{left:0;top:0;width:1200px;height:620px;
  background:linear-gradient(180deg,#5b6672 0%,#7a7f86 28%,#8a6d4b 58%,#a0865f 74%,#e9e4dc 90%,#ffffff 100%)}
.social-dot{width:16px;height:16px;border-radius:50%;border:2px solid var(--white)}
.brand{left:540px;top:20px;width:120px;height:88px;display:flex;align-items:center;justify-content:center}
.brand-name{font-weight:700;font-size:17px;color:var(--white);text-align:center;line-height:1.1}
.burger span{display:block;width:22px;height:2px;background:var(--white);margin-bottom:6px}
.nav{left:60px;top:132px;width:1080px;height:30px;border-bottom:1px solid rgba(255,255,255,.75);
  display:flex;justify-content:space-between;padding:0 22px}
.nav a{font-size:15px;font-weight:700;color:var(--white)}
.hero-kicker{left:0;width:1200px;top:258px;text-align:center;color:var(--white);font-size:29px;font-weight:400}
.hero-title{left:0;width:1200px;top:296px;text-align:center;color:var(--white);font-size:60px;font-weight:900;letter-spacing:.3px}
.btn{background:var(--gold);color:var(--white);border-radius:20px;font-size:14px;font-weight:500;
  display:flex;align-items:center;justify-content:center;text-transform:uppercase}
.slide-arrow{width:32px;height:32px;border-radius:50%;background:var(--teal);display:flex;align-items:center;justify-content:center}

/* Section headings */
.peak{width:66px;height:30px;left:567px}
.section-title{left:0;width:1200px;text-align:center;font-size:31px;font-weight:500;color:var(--ink)}
.about-copy{left:136px;top:742px;width:928px;font-size:16.5px;line-height:23px;color:var(--text);text-align:justify;letter-spacing:.2px}
.about-end{left:136px;top:880px;width:928px;font-size:16.5px;line-height:23px;color:var(--text);text-align:center;letter-spacing:.2px}

/* Holiday */
.ghost-word{left:420px;top:1090px;font-size:96px;font-weight:700;color:#f2f2f2;letter-spacing:2px;line-height:1}
.hol-kicker{left:60px;top:1160px;font-size:27px;font-weight:400}
.hol-big{left:58px;font-family:"Heebo",sans-serif;font-weight:700;font-size:76px;line-height:1}
.hol-copy{left:59px;top:1384px;width:570px;font-size:15.5px;line-height:23px;color:var(--text);text-align:justify;letter-spacing:.8px}
.hol-photo{left:720px;top:1090px;width:480px;height:500px;
  background:radial-gradient(closest-side at 55% 55%,#8a6a52 0%,#b59a84 45%,#e2dcd6 75%,rgba(255,255,255,0) 100%)}

/* Tours */
.tours{left:60px;top:1721px;width:1080px;height:443px;display:flex}
.tour{flex:1;position:relative}
.tour span{position:absolute;left:0;right:0;bottom:14px;text-align:center;color:var(--white);font-size:19px;font-weight:400}

/* Video */
.video{left:0;top:2238px;width:1200px;height:299px;
  background:linear-gradient(180deg,#7d8a96 0%,#55614f 35%,#2d3a2c 60%,#2aa0c0 78%,#1d5b6a 100%)}
.play{left:570px;top:2356px;width:64px;height:64px;border-radius:50%;background:var(--white);display:flex;align-items:center;justify-content:center}

/* Testimonials */
.t-card{top:2793px;height:149px;background:var(--white);box-shadow:0 0 22px rgba(0,0,0,.06);padding:50px 0 0 46px}
.t-card p{font-size:11px;line-height:20px;color:var(--muted);width:360px}
.t-name{font-family:"Libre Baskerville",serif;font-size:11px;font-weight:700;color:#333;margin-top:4px}
.t-role{font-family:"Libre Baskerville",serif;font-size:8.5px;font-style:italic;color:var(--gold)}
.avatar{width:76px;height:76px;border-radius:50%;background:linear-gradient(160deg,#c9c2bb,#5a4a42)}

/* Newsletter */
.sub-line{left:0;width:1200px;top:3090px;text-align:center;font-size:16px;color:#555;letter-spacing:.3px}
.email{left:301px;top:3143px;width:455px;height:48px;border:1px solid #cfcfcf;border-radius:8px 0 0 8px;
  font-size:14px;color:#9d9d9d;padding:0 16px;display:flex;align-items:center}
.subscribe{left:750px;top:3143px;width:155px;height:48px;background:var(--gold);border-radius:0 24px 24px 0;
  color:var(--white);font-weight:700;font-size:17px;display:flex;align-items:center;justify-content:center}
.backpacker{left:0;top:2995px;width:122px;height:395px;background:linear-gradient(180deg,#ffffff,#c79a6a 30%,#8a5e36 55%,#7d8ca2 85%,#e8ecf0)}
.townscape{left:880px;top:3000px;width:320px;height:200px;
  background:radial-gradient(closest-side at 70% 50%,#a8542a 0%,#c98b5c 45%,rgba(255,255,255,0) 100%)}

/* Call band */
.call-text{left:250px;top:3256px;font-size:40px;font-weight:400;color:#222}
.call-text b{color:var(--teal);font-weight:500}
.call-num{left:826px;top:3250px;font-size:35px;font-weight:400;color:#222;letter-spacing:1px}
.call-sub{left:826px;top:3290px;font-size:13px;color:#555}
.call-rule{left:152px;top:3344px;width:876px;height:1px;background:var(--gold)}

/* Footer */
.footer{left:0;top:3390px;width:1200px;height:222px;background:var(--footer)}
.to-top{left:575px;top:3365px;width:56px;height:56px;border-radius:50%;background:var(--gold);display:flex;align-items:center;justify-content:center}
.foot-nav{left:136px;top:3470px;width:928px;display:flex;justify-content:space-between;font-size:16px;color:#333}
.foot-rule{left:253px;top:3525px;width:682px;height:1px;background:#dcdcdc}
.foot-dot{width:14px;height:14px;border-radius:50%;background:var(--teal)}
</style>
</head>
<body>

<header>
  <div class="abs hero" role="img" aria-label="Family of hikers with backpacks beside an off-road vehicle on a snowy mountain plateau"></div>
  <div class="abs social-dot" style="left:58px;top:52px"></div>
  <div class="abs social-dot" style="left:99px;top:52px"></div>
  <div class="abs brand"><span class="brand-name">Wayfarer<br>Travel Co.</span></div>
  <div class="abs burger" style="left:1113px;top:54px"><span></span><span></span><span style="width:16px;margin-left:6px"></span></div>
  <nav class="abs nav">
    <a href="#">HOME</a><a href="#">ABOUT US</a><a href="#">BRAMBLETON VACATIONS</a><a href="#">FAMILY TRIPS</a><a href="#">ROAD TRIPS</a><a href="#">OTHER DESTINATIONS</a><a href="#">CONTACT US</a>
  </nav>
  <p class="abs hero-kicker">HELPING TEXAS FAMILIES</p>
  <h1 class="abs hero-title">CREATE MAGICAL VACATIONS</h1>
  <a class="abs btn" href="#" style="left:522px;top:391px;width:156px;height:32px">Plan My Trip</a>
  <div class="abs slide-arrow" style="left:45px;top:306px"><svg width="12" height="12" viewBox="0 0 12 12"><path d="M8 1 L3 6 L8 11" stroke="#fff" stroke-width="1.6" fill="none"/></svg></div>
  <div class="abs slide-arrow" style="left:1124px;top:306px"><svg width="12" height="12" viewBox="0 0 12 12"><path d="M4 1 L9 6 L4 11" stroke="#fff" stroke-width="1.6" fill="none"/></svg></div>
</header>

<section>
  <svg class="abs peak" style="top:640px" viewBox="0 0 66 30" aria-hidden="true"><path d="M2 28 L22 8 L30 16 L40 2 L64 28" stroke="#222" stroke-width="1.6" fill="none"/><path d="M18 28 L30 16 M40 2 L36 12" stroke="#222" stroke-width="1" fill="none"/></svg>
  <h2 class="abs section-title" style="top:685px">About Us</h2>
  <p class="abs about-copy">Lorem Ipsum is simply dummy text of the printing and typesetting industry. Lorem Ipsum has been the industry's standard dummy text ever since the 1500s, when an unknown printer took a galley of type and scrambled it to make a type specimen book. It has survived not only five centuries, but also the leap into electronic typesetting, remaining essentially unchanged. It was popularised in the 1960s with the release of Inkline sheets containing Lorem Ipsum passages, and more recently with desktop publishing software like Pagewright Studio including versions of Lorem Ipsum.&nbsp; It has survived not only five centuries, but also the leap into electronic typesetting, remaining essentially</p>
  <p class="abs about-end">unchanged.</p>
  <a class="abs btn" href="#" style="left:522px;top:929px;width:156px;height:35px">Learn More</a>
</section>

<section>
  <div class="abs ghost-word" aria-hidden="true">Brambleton</div>
  <div class="abs hol-photo" role="img" aria-label="Smiling family of three waving in front of a fairytale castle"></div>
  <p class="abs hol-kicker">We Make Your</p>
  <p class="abs hol-big" style="top:1200px;color:var(--teal)">Holiday</p>
  <p class="abs hol-big" style="top:1288px;color:var(--ink)">Awesome</p>
  <p class="abs hol-copy">As the forerunner of Tibet inbound tourism since 1984, Tibet is a Lhasa-based Tibet tour operator, specializing in Small group and private package tours.</p>
  <a class="abs btn" href="#" style="left:60px;top:1482px;width:157px;height:35px">Plan My Trip</a>
</section>

<section>
  <svg class="abs peak" style="top:1592px" viewBox="0 0 66 30" aria-hidden="true"><path d="M2 28 L22 8 L30 16 L40 2 L64 28" stroke="#222" stroke-width="1.6" fill="none"/><path d="M18 28 L30 16 M40 2 L36 12" stroke="#222" stroke-width="1" fill="none"/></svg>
  <h2 class="abs section-title" style="top:1637px">Popular Tours</h2>
  <div class="abs tours">
    <a class="tour" href="#" role="img" aria-label="Mother and daughter facing a fairytale castle at sunset" style="background:linear-gradient(180deg,#8fb3d6 0%,#d9b48a 45%,#8a5a3a 100%)"><span>Brambleton Vacations</span></a>
    <a class="tour" href="#" role="img" aria-label="Family of four smiling outdoors in golden light" style="background:linear-gradient(180deg,#cfd3c7 0%,#8c8a63 50%,#4f4b3a 100%)"><span>Family Trips</span></a>
    <a class="tour" href="#" role="img" aria-label="Couple reading a map on the hood of a car" style="background:linear-gradient(180deg,#d9dfd0 0%,#7f8a6a 50%,#5a5c58 100%)"><span>Road Trips</span></a>
    <a class="tour" href="#" role="img" aria-label="Couple holding roses at a colourful tropical destination" style="background:linear-gradient(180deg,#d8c46a 0%,#8a7f86 45%,#6a4a52 100%)"><span>Other Destinations</span></a>
  </div>
</section>

<section>
  <div class="abs video" role="img" aria-label="Turquoise mountain lake surrounded by snowy forested peaks"></div>
  <div class="abs play"><svg width="24" height="24" viewBox="0 0 24 24"><path d="M7 4 L19 12 L7 20 Z" stroke="#555" stroke-width="1.6" fill="none" stroke-linejoin="round"/></svg></div>
</section>

<section>
  <svg class="abs peak" style="top:2615px" viewBox="0 0 66 30" aria-hidden="true"><path d="M2 28 L22 8 L30 16 L40 2 L64 28" stroke="#222" stroke-width="1.6" fill="none"/><path d="M18 28 L30 16 M40 2 L36 12" stroke="#222" stroke-width="1" fill="none"/></svg>
  <h2 class="abs section-title" style="top:2660px">Traveller's Experiences</h2>
  <svg class="abs" style="left:245px;top:2860px" width="38" height="24" viewBox="0 0 38 24" aria-hidden="true"><path d="M36 12 H3 M13 2 L3 12 L13 22" stroke="#555" stroke-width="1.5" fill="none"/></svg>
  <article class="abs t-card" style="left:329px;width:427px">
    <p>Ex ea commodo consequat. Duis aute irure dolor reprehenderit in voluptate velit esse cillut fugiat nulla official.</p>
    <p class="t-name">Owen Hartley</p>
    <p class="t-role">Writer at Lantern Films</p>
  </article>
  <div class="abs avatar" style="left:365px;top:2747px" role="img" aria-label="Portrait of traveller Owen Hartley"></div>
  <article class="abs t-card" style="left:848px;width:400px">
    <p style="white-space:nowrap">Auctor mauris enim lorem fames fames fermentum fusce sapien</p>
    <p>mi, consectetuer. Justo ornare. Sociis permalesuada, et urna.</p>
    <p class="t-name">Mara Delgado</p>
    <p class="t-role">Creative Director at Brightfold</p>
  </article>
  <div class="abs avatar" style="left:873px;top:2747px" role="img" aria-label="Portrait of traveller Mara Delgado"></div>
</section>

<section>
  <div class="abs backpacker" role="img" aria-label="Young traveller with a backpack looking ahead"></div>
  <div class="abs townscape" role="img" aria-label="Hillside old town with terracotta rooftops"></div>
  <svg class="abs peak" style="top:2995px" viewBox="0 0 66 30" aria-hidden="true"><path d="M2 28 L22 8 L30 16 L40 2 L64 28" stroke="#222" stroke-width="1.6" fill="none"/><path d="M18 28 L30 16 M40 2 L36 12" stroke="#222" stroke-width="1" fill="none"/></svg>
  <h2 class="abs section-title" style="top:3040px">Get Updates &amp; More</h2>
  <p class="abs sub-line">Thoughtful thoughts to your inbox</p>
  <div class="abs email">Enter your email</div>
  <div class="abs subscribe">SUBSCRIBE</div>

  <svg class="abs" style="left:150px;top:3262px" width="62" height="60" viewBox="0 0 62 60" aria-hidden="true">
    <path d="M14 6 L22 16 L17 22 C20 32 28 40 38 43 L44 38 L54 46 L48 55 C28 54 8 34 6 14 Z" stroke="#b47510" stroke-width="2" fill="none" stroke-linejoin="round"/>
    <path d="M34 8 A18 18 0 0 1 52 26 M34 16 A10 10 0 0 1 44 26" stroke="#b47510" stroke-width="2" fill="none"/>
  </svg>
  <p class="abs call-text">Call us for the <b>Best Deals</b></p>
  <p class="abs call-num">222.555.0148</p>
  <p class="abs call-sub">Toll Free &amp; 24/7 Available</p>
  <div class="abs call-rule"></div>
</section>

<footer>
  <div class="abs footer"></div>
  <a class="abs to-top" href="#"><svg width="22" height="14" viewBox="0 0 22 14"><path d="M2 12 L11 3 L20 12" stroke="#fff" stroke-width="2" fill="none"/></svg></a>
  <nav class="abs foot-nav">
    <a href="#">Home</a><a href="#">About Us</a><a href="#">Brambleton Vacations</a><a href="#">Family Trips</a><a href="#">Road Trips</a><a href="#">Other Destinations</a><a href="#">Contact Us</a>
  </nav>
  <div class="abs foot-rule"></div>
  <div class="abs foot-dot" style="left:562px;top:3564px"></div>
  <div class="abs foot-dot" style="left:593px;top:3564px"></div>
  <div class="abs foot-dot" style="left:624px;top:3564px"></div>
</footer>

</body>
</html>
```